We need a single web page design for a promotion. This page will acts as a landing page for users. Please provide us with a cutting edge design. I have attached a previous design used a couple of years ago.

Link: http://www.brightkettlestudio.example/freegift/

The Start Here box needs to look like this:

-Start Here (heading) 
-A box for email addresses to be entered
-Then a check box with "Yes, I have read and agree to the Privacy Policy and agree to receive email marketing from Bright Kettle Studio and acknowledge that I will receive special email offers from our marketing partners, including the Harbor Ledger newsletter."
-A submit button 

All of this information needs to be in one box please.  And please feel free to contact me if you have any questions about this. 

Target Market(s)

Middle aged women (housewives)

Requirements
Must have
• Images must reflect the "500 Photo Prints". The only fields that are necessary are a box for email and a submit button.
Should not have
• The word FREE anywhere on the page

```html
<!DOCTYPE html>
<html lang="en">
<head>
<meta charset="utf-8">
<title>Bright Kettle Studio – 500 Photo Prints</title>
<link rel="stylesheet" href="https://fonts.googleapis.com/css2?family=Montserrat:wght@300;400;700&family=Roboto:wght@400;700&family=Roboto+Condensed:wght@700;800&display=swap">
<style>
  :root {
    --bg-core: #1f5a7c;
    --bg-mid: #0e2c44;
    --bg-edge: #050f1b;
    --ink-light: #ffffff;
    --ink-soft: #e6eef4;
    --ink-dark: #222a30;
    --brand-blue: #0e5a8c;
    --brand-blue-deep: #0a3f66;
    --panel-top: #ffffff;
    --panel-bottom: #dcdfe2;
    --field: #e4e6e8;
    --field-line: #c3c7cb;
    --frame: #f7f7f5;
  }
  * { box-sizing: border-box; margin: 0; padding: 0; }
  html, body { width: 1200px; height: 800px; overflow: hidden; background: var(--bg-edge); }
  .landing {
    position: relative;
    width: 1200px;
    height: 800px;
    overflow: hidden;
    background: radial-gradient(ellipse 620px 520px at 600px 390px, var(--bg-core) 0%, var(--bg-mid) 55%, var(--bg-edge) 100%);
    font-family: "Montserrat", "Helvetica Neue", Arial, sans-serif;
    color: var(--ink-light);
  }
  .headline {
    position: absolute;
    top: 28px; left: 0; width: 100%;
    text-align: center;
    font-size: 42px;
    font-weight: 300;
    letter-spacing: -0.5px;
    text-shadow: 0 0 14px rgba(255,255,255,0.35);
  }
  .headline strong { font-weight: 700; }

  .collage { position: absolute; inset: 0; }
  .print {
    position: absolute;
    border: 7px solid var(--frame);
    box-shadow: 0 4px 14px rgba(0,0,0,0.55);
  }
  .print--back-left  { left: 214px; top: 112px; width: 262px; height: 250px; transform: rotate(-16deg); background: linear-gradient(160deg,#e8ddd2,#b9a796); }
  .print--far-left   { left: 170px; top: 232px; width: 190px; height: 210px; transform: rotate(-22deg); background: linear-gradient(150deg,#cfc2b4,#8f7f70); }
  .print--back-right { left: 742px; top: 116px; width: 170px; height: 140px; transform: rotate(-24deg); background: linear-gradient(160deg,#e6e0d8,#b8aa9b); }
  .print--mother     { left: 330px; top: 148px; width: 296px; height: 410px; transform: rotate(8deg); background: linear-gradient(170deg,#4b3327 0%,#c99a82 38%,#7fa58d 80%,#5c7e6a 100%); }
  .print--family     { left: 512px; top: 138px; width: 258px; height: 440px; transform: rotate(-3deg); background: linear-gradient(165deg,#d9c4a6 0%,#e8b9a3 40%,#d9a7b6 75%,#c78da3 100%); }
  .print--camera     { left: 770px; top: 176px; width: 206px; height: 262px; transform: rotate(5deg); background: linear-gradient(165deg,#d7c8b8 0%,#c9a189 45%,#a9b2bd 75%,#8d7d70 100%); }

  .signup {
    position: absolute;
    left: 216px; top: 434px;
    width: 775px; height: 147px;
    border-radius: 10px;
    background: linear-gradient(180deg, var(--panel-top) 0%, var(--panel-bottom) 100%);
    box-shadow: 0 6px 18px rgba(0,0,0,0.55);
    color: var(--ink-dark);
  }
  .signup__title {
    position: absolute;
    left: 18px; top: 10px;
    font-family: "Roboto Condensed", "Arial Narrow", Arial, sans-serif;
    font-weight: 800;
    font-size: 48px;
    line-height: 48px;
    letter-spacing: -0.5px;
    color: var(--brand-blue);
    white-space: nowrap;
  }
  .signup__prompt {
    position: absolute;
    left: 18px; top: 58px;
    font-family: "Roboto Condensed", "Arial Narrow", Arial, sans-serif;
    font-weight: 700;
    font-size: 23px;
    line-height: 26px;
    color: var(--brand-blue);
    white-space: nowrap;
  }
  .email-field {
    position: absolute;
    left: 18px; top: 100px;
    width: 260px; height: 30px;
    border: 1px solid var(--field-line);
    border-radius: 5px;
    background: var(--field);
    box-shadow: inset 0 1px 3px rgba(0,0,0,0.15);
  }

  .consent {
    position: absolute;
    left: 470px; top: 18px;
    width: 290px;
    display: flex;
    gap: 9px;
    font-family: "Roboto", Arial, sans-serif;
    font-size: 11px;
    line-height: 15px;
    color: var(--ink-dark);
  }
  .consent__box {
    flex: none;
    width: 10px; height: 10px;
    margin-top: 2px;
    border: 1px solid #777;
    border-radius: 2px;
    background: #fff;
  }
  .consent a { color: var(--ink-dark); text-decoration: underline; }
  .brand {
    position: absolute;
    left: 488px; top: 104px;
    display: flex;
    align-items: center;
    gap: 5px;
    font-family: "Roboto", Arial, sans-serif;
    font-size: 10px;
    color: var(--brand-blue);
  }
  .brand__mark { width: 14px; height: 14px; border-radius: 2px; background: var(--brand-blue); }
  .submit {
    position: absolute;
    left: 642px; top: 94px;
    width: 108px; height: 34px;
    border: none;
    border-radius: 17px;
    background: linear-gradient(180deg, #1a6ea6 0%, var(--brand-blue-deep) 100%);
    box-shadow: 0 2px 4px rgba(0,0,0,0.35);
    color: #fff;
    font-family: "Roboto", Arial, sans-serif;
    font-weight: 700;
    font-size: 16px;
  }

  .benefits {
    position: absolute;
    top: 620px; left: 0; width: 100%;
    text-align: center;
    font-size: 21px;
    font-weight: 300;
    letter-spacing: -0.3px;
    color: var(--ink-soft);
  }
  .benefits .divider { margin: 0 9px; }

  .fine-print {
    position: absolute;
    top: 678px; left: 216px; width: 768px;
    text-align: center;
    font-family: "Roboto", Arial, sans-serif;
    font-size: 8.6px;
    line-height: 10.6px;
    color: var(--ink-soft);
  }
  .fine-print p + p { margin-top: 8px; }
  .fine-print .notice { text-transform: uppercase; }
</style>
</head>
<body>
<main class="landing">
  <h1 class="headline">Get 500 photo Prints <strong>Delivered to You</strong></h1>

  <section class="collage" aria-label="Scattered photo prints">
    <div class="print print--back-left" role="img" aria-label="Photo print of a warm indoor kitchen scene"></div>
    <div class="print print--far-left" role="img" aria-label="Photo print of a family at home"></div>
    <div class="print print--back-right" role="img" aria-label="Photo print of a kitchen interior"></div>
    <div class="print print--mother" role="img" aria-label="Photo print of a smiling mother"></div>
    <div class="print print--family" role="img" aria-label="Photo print of a smiling girl beside her father"></div>
    <div class="print print--camera" role="img" aria-label="Photo print of a father holding a digital camera"></div>
  </section>

  <form class="signup" action="http://www.brightkettlestudio.example/freegift/">
    <h2 class="signup__title">START HERE</h2>
    <p class="signup__prompt">Enter your Email Address</p>
    <span class="email-field" aria-label="Email address field"></span>

    <div class="consent">
      <span class="consent__box" aria-hidden="true"></span>
      <p>YES, I have read and agree to the <a href="#">Privacy Policy</a> and agree to receive email marketing from Bright Kettle Studio and acknowledge that I will receive special email offers from our marketing partners, including the Harbor Ledger newsletter.</p>
    </div>
    <span class="brand"><span class="brand__mark" aria-hidden="true"></span>BrightKettleStudio.example</span>
    <button class="submit" type="button">Submit</button>
  </form>

  <p class="benefits">Professional Quality Photos<span class="divider">|</span>Unlimited Storage<span class="divider">|</span>Share With Your Friends</p>

  <footer class="fine-print">
    <p class="notice">*Offer redemption will require participation and / or purchase of third party offers.</p>
    <p>To receive the membership incentive gift of Five Hundred (500) photo prints you must complete all of the steps outlined herein. Prospective members must: (a) submit their zip code to determine geographic eligibility; (b) register with a valid and deliverable email address; (c) submit accurate contact and demographic information including a mailing address; (d) Accumulate a total of Twenty Five (25) points by either answering survey questions, completing lead questionnaires, or taking advantage of 3rd party offers. Purchase may be required. Please read participation requirements for details.</p>
    <p>On each page, you will be able to see your current point total and the total number of points necessary to redeem the incentive gift. Upon completion of all requirements and upload of the necessary photos, we will ship the incentive gift to you at no shipping cost. Unless otherwise indicated, participation eligibility is restricted to US residents, 18 and over. Void where prohibited.</p>
  </footer>
</main>
</body>
</html>
```